Modern card design needed for building development company

We are looking for a sharp modern new look for our business cards.
We are a New Zealand based company called TKV Ventures NZ LTD that specialises in subdividing large sections, housing and commercial buildings.
We have attached a photo of the current logo and would like to see it improved somehow as it looks a bit dated.
We are open to any colours.

Target Market(s)

Investors, Property buyers

Industry/Entity Type

Investment

Contact Information for Business Card

TKV VENTURES NZ LTD
www.tkvventuresnz.co.nz

Howard Pennick
Phone +64 21 843 192
Email hdpennick@fernmail.co.nz

Font styles to use
Serif
Sans Serif

Colors
0792cd
33a6d7
85cae6
6b449b
886aae
f04a50
ec1f27
f37122
f68d4d

Requirements
Must have
• Please try and make the logo more modern or if you have a similar one we would like to see it.

```html
<!DOCTYPE html>
<html lang="en">
<head>
<meta charset="utf-8">
<title>TKV Ventures NZ LTD – Business Card</title>
<link rel="stylesheet" href="https://fonts.googleapis.com/css2?family=Jost:wght@300;400&family=Montserrat:wght@800&display=swap">
<style>
  :root {
    --paper: #ffffff;
    --card-orange: #f68d4d;
    --ink: #231f20;
    --mark-mauve: #a96f74;
    --mark-brown: #b07f64;
  }
  * { margin: 0; padding: 0; box-sizing: border-box; }
  html, body { width: 1200px; height: 1059px; overflow: hidden; background: var(--paper); }
  .sheet { position: relative; width: 1200px; height: 1059px; }
  .card {
    position: absolute; width: 564px; background: var(--card-orange);
    color: var(--ink); font-family: "Jost", sans-serif; text-align: center;
  }
  .card--front { left: 0; top: 6px; height: 983px; }
  .card--back { left: 636px; top: 0; height: 973px; }
  .line { position: absolute; left: 0; right: 0; white-space: nowrap; line-height: 1; }
  .contact-name { top: 84px; font-size: 37px; font-weight: 400; }
  .contact-phone { top: 124px; font-size: 29px; font-weight: 300; }
  .contact-email { top: 157px; font-size: 24px; font-weight: 300; }
  .wordmark { color: var(--mark-mauve); font-family: "Jost", sans-serif; font-weight: 400; }
  .wordmark-top { font-size: 68px; letter-spacing: 4px; }
  .wordmark-bottom { font-size: 38px; letter-spacing: 3px; }
  .card--front .wordmark-top { top: 427px; }
  .card--front .wordmark-bottom { top: 502px; }
  .card--back .wordmark-top { top: 421px; }
  .card--back .wordmark-bottom { top: 497px; }
  .mark-square { position: absolute; left: 50%; width: 130px; height: 130px; margin-left: -65px; background: var(--mark-brown); }
  .card--front .mark-square { top: 620px; }
  .card--back .mark-square { top: 615px; }
  .company-name { top: 856px; font-family: "Montserrat", sans-serif; font-weight: 800; font-size: 23px; letter-spacing: 1px; }
  .company-web { top: 884px; font-size: 30px; font-weight: 300; }
  .service { font-size: 29px; font-weight: 300; }
  .label {
    position: absolute; font-family: Arial, Helvetica, sans-serif; font-size: 41px;
    color: var(--ink); width: 300px; text-align: center; line-height: 1;
  }
  .label--front { left: 132px; top: 1002px; }
  .label--back { left: 777px; top: 1014px; }
</style>
</head>
<body>
<div class="sheet">
  <section class="card card--front">
    <p class="line contact-name">Howard Pennick</p>
    <p class="line contact-phone">+64 21 843 192</p>
    <p class="line contact-email">Email : hdpennick@fernmail.co.nz</p>
    <p class="line wordmark wordmark-top">TKV</p>
    <p class="line wordmark wordmark-bottom">VENTURES NZ LTD</p>
    <div class="mark-square"></div>
    <p class="line company-name">TKV VENTURES NZ LTD</p>
    <p class="line company-web">www.tkvventuresnz.co.nz</p>
  </section>
  <section class="card card--back">
    <p class="line service" style="top:160px">HOUSING</p>
    <p class="line service" style="top:195px">COMMERCIAL BUILDING</p>
    <p class="line service" style="top:263px">SPECIALISES</p>
    <p class="line service" style="top:296px">IN</p>
    <p class="line service" style="top:330px">SUB DIVIDING LARGE SECTION</p>
    <p class="line wordmark wordmark-top">TKV</p>
    <p class="line wordmark wordmark-bottom">VENTURES NZ LTD</p>
    <div class="mark-square"></div>
  </section>
  <p class="label label--front">FRONT</p>
  <p class="label label--back">BACK</p>
</div>
</body>
</html>
```